Domestic violence resource cards for distribution to at-risk patients in an emergency department

Using the attached image(or very similar) and text document, a tri-fold business card is requested that integrates the image on the outside and the document content throughout the card's remaining faces. A creative format is requested, one that does not look like the typical cold, uncaring bullet point outlines that are found in similar resource projects. Bold or larger font sizes are requested for headings and body text is not required to be aligned or justified and the bullet points in the supplied document can be removed for creative license. Palattes should be clear, avoiding neons or implied target gender. Legibility is paramount, but again a creative presentation of a very serious subject is our goal. These cards are intended to be distributed to patients or others in the emergency department that may benefit from domestic violence resources. The business card size is mandatory so that the card can be concealed if needed by the receiver.
Updates

Reason: There are several revisions from designers that we are anxiously awaiting; we want to provide time for these designers to submit new designs but also continue spending time with their families and friends around the holiday season.

Target Market(s)

Patients and family in contact with emergency services

Industry/Entity Type

Healthcare

Contact Information for Business Card

Double sided tri-fold card with image on outer sides, text content and resource phone numbers on the exterior. When complete, the card should fold to standard US business card size.

Font styles to use
Other font styles liked:
• Designer's choice, but clear and legible

Requirements
Must have
• See above description. Card must be tri-fold, fold down to standard business card size, remain easily readable, and fold along the long edge.
Should not have
• Cartoon images; bloated fonts or clipart; bright, flashy neon or rainbow-like colors; additional graphics or charts.

```html
<!DOCTYPE html>
<html lang="en">
<head>
<meta charset="utf-8">
<title>Domestic Violence Resource Card</title>
<link href="https://fonts.googleapis.com/css2?family=Didact+Gothic&family=Montserrat:wght@600;700&display=swap" rel="stylesheet">
<style>
  :root{
    --ink:#111;
    --black:#0b0b0b;
    --paper:#ffffff;
    --grey:#6b6b6b;
    --mid:#3f3f3f;
    --frame:#9a9a9a;
    --faint:#efefef;
    --bg:#e4e4e4;
  }
  *{box-sizing:border-box;margin:0;padding:0}
  html,body{width:1200px;height:1200px;overflow:hidden}
  body{background:var(--bg);font-family:"Didact Gothic",sans-serif;color:var(--ink);position:relative}
  .card{position:absolute;box-shadow:0 4px 12px rgba(0,0,0,.25);overflow:hidden;background:var(--paper)}
  .folded{left:60px;top:110px;width:360px;height:206px}
  .spread{left:60px;width:1080px;height:206px}
  .outside{top:360px}
  .inside{top:660px}
  .panel{position:absolute;top:0;width:360px;height:206px}
  .p1{left:0}.p2{left:360px}.p3{left:720px}
  .bg{position:absolute;inset:0}

  /* cover */
  .cover{background:var(--black)}
  .cover-frame{position:absolute;inset:14px;border:1.5px solid var(--frame)}
  .cover-box{position:absolute;inset:22px;background:var(--mid);overflow:hidden}
  .cover-photo{position:absolute;left:0;top:0;bottom:0;width:62%;
    background:radial-gradient(ellipse at 45% 55%,#b9b9b9 0%,#7a7a7a 40%,#3f3f3f 75%)}
  .cover-title{position:absolute;right:14px;top:26px;text-align:right;color:#fff;
    font-family:"Montserrat",sans-serif;font-weight:700;font-size:27px;line-height:1.06;letter-spacing:.5px}
  .cover-url{position:absolute;right:14px;top:128px;font-size:7px;color:#bbb;border-top:1px solid #888;padding-top:3px;width:120px;text-align:right}

  /* text */
  h2{font-family:"Montserrat",sans-serif;font-weight:700;font-size:11.5px;line-height:1.1}
  .sub{font-size:10px;margin-bottom:4px}
  ul{list-style:none}
  .tips li{font-size:9.6px;line-height:1.22;margin-bottom:1px;padding-left:11px;position:relative}
  .tips li::before{content:"➢";position:absolute;left:0;font-size:8px}
  .tips-left{position:absolute;left:12px;top:12px;width:336px}
  .resources{position:absolute;left:14px;top:14px;width:340px}
  .resources li{font-size:9.6px;line-height:1.25;margin-bottom:5px;padding-left:11px;position:relative}
  .resources li::before{content:"✦";position:absolute;left:0;font-size:8px}
  .resources b{font-family:"Montserrat",sans-serif;font-weight:600;font-size:9px}
  .site{position:absolute;right:14px;bottom:12px;color:#fff;font-family:"Montserrat",sans-serif;font-weight:600;font-size:12px;letter-spacing:1px}

  .watermark{position:absolute;inset:0;color:var(--faint);font-family:"Montserrat",sans-serif;font-weight:700;font-size:22px;line-height:1.2;overflow:hidden;white-space:nowrap;transform:rotate(-8deg);transform-origin:center}
  .watermark.right{transform:rotate(18deg)}
  .ask{position:absolute;left:12px;top:10px;width:340px}
  .ask li{font-size:10px;line-height:1.2;padding-left:11px;position:relative}
  .ask li::before{content:"▲";position:absolute;left:0;font-size:6px;top:2px}
  .banner{position:absolute;left:10px;bottom:12px;color:#fff;font-size:11px;letter-spacing:.8px}
  .banner strong{font-family:"Montserrat",sans-serif;font-weight:700;font-style:italic;font-size:13px}
  .remember{position:absolute;left:0;right:0;top:16px;text-align:center}
  .remember h2{font-size:14px;margin-bottom:6px}
  .remember li{font-size:10.5px;line-height:1.4}
  .remember li::before{content:"✓ ";font-size:9px}
  .tips-right{position:absolute;right:12px;top:14px;width:330px;text-align:right}
  .tips-right li{font-size:9.6px;line-height:1.22;margin-bottom:2px;padding-right:11px;position:relative}
  .tips-right li::after{content:"◂";position:absolute;right:0}
</style>
</head>
<body>

<!-- folded front -->
<section class="card folded cover" aria-label="Folded card front">
  <div class="cover-frame"></div>
  <div class="cover-box">
    <div class="cover-photo" role="img" aria-label="Black and white photograph of clenched hands with wrists bound by rope"></div>
    <div class="cover-title">National<br>Domestic<br>Violence</div>
    <div class="cover-url">www.safeharborshelters.org</div>
  </div>
</section>

<!-- outside spread -->
<section class="card spread outside" aria-label="Outside of card">
  <svg class="bg" width="1080" height="206" viewBox="0 0 1080 206">
    <rect width="1080" height="206" fill="#fff"/>
    <rect x="0" y="190" width="410" height="16" fill="#6b6b6b"/>
    <path d="M410 206 L410 180 C560 175 660 120 720 40 L720 0 L1080 0 L1080 206 Z" fill="#0b0b0b"/>
  </svg>
  <div class="panel p1">
    <div class="tips-left">
      <h2>Leaving Can Be Tough And Very Dangerous.</h2>
      <p class="sub">Here are some tips to help you plan for safety:</p>
      <ul class="tips">
        <li>Stay off social media or cancel your accounts so that you can't be found online or through your friends</li>
        <li>Do not talk about your plans in public areas or in mixed groups</li>
        <li>Open a credit card or bank account in your name only and do not use it until you are ready</li>
        <li>Keep a charged prepaid cell phone and a shelter hotline number ready for emergencies</li>
        <li>Review your plan often and only share with trusted friends or family</li>
        <li>Be careful: you are at most risk during the first 72 hours after leaving an abusive situation</li>
        <li>Seek help at a police station, firehouse or hospital if needed</li>
      </ul>
    </div>
  </div>
  <div class="panel p2">
    <ul class="resources">
      <li>Nationwide Family Safety Line <b>1-800-555-0142</b></li>
      <li>Safe Haven House: Domestic Violence Crisis Resource <b>303-555-0118</b></li>
      <li>Threshold Domestic Violence Resources <b>303-555-0127</b></li>
      <li>The Harbor Crisis Center <b>1-888-555-0163</b></li>
      <li>Family Roots Violence Resources <b>303-555-0174</b></li>
      <li>Quiet Bench: Sexual Assault Victim's Advocate <b>303-555-0185</b></li>
      <li>Respect First: Teen Dating Resource<br><b>1-866-555-0196 or text "respect" to 55500</b></li>
    </ul>
    <div class="site">www.safeharborshelters.org</div>
  </div>
  <div class="panel p3 cover">
    <div class="cover-frame"></div>
    <div class="cover-box">
      <div class="cover-photo" role="img" aria-label="Black and white photograph of clenched hands with wrists bound by rope"></div>
      <div class="cover-title">National<br>Domestic<br>Violence</div>
      <div class="cover-url">www.safeharborshelters.org</div>
    </div>
  </div>
</section>

<!-- inside spread -->
<section class="card spread inside" aria-label="Inside of card">
  <svg class="bg" width="1080" height="206" viewBox="0 0 1080 206">
    <rect width="1080" height="206" fill="#fff"/>
    <rect x="0" y="188" width="1080" height="18" fill="#6b6b6b"/>
    <path d="M0 164 L320 164 L340 188 L340 206 L0 206 Z" fill="#0b0b0b"/>
    <rect x="0" y="188" width="340" height="18" fill="#0b0b0b"/>
    <rect x="900" y="188" width="180" height="18" fill="#0b0b0b"/>
    <line x1="720" y1="0" x2="720" y2="206" stroke="#d8d8d8" stroke-width="1"/>
  </svg>
  <div class="panel p1">
    <div class="watermark" aria-hidden="true">National Domestic Violence<br>National Domestic Violence<br>National Domestic Violence<br>National Domestic Violence<br>National Domestic Violence<br>National Domestic Violence</div>
    <div class="ask">
      <h2>Does Your Partner Ever...</h2>
      <ul>
        <li>Hit, kick, push, choke or slap you?</li>
        <li>Intimidate you with weapons or harmful objects?</li>
        <li>Force you to engage in sexual acts?</li>
        <li>Threaten to hurt you, your children or your friends/family?</li>
        <li>Threaten to deport you or tell others your personal information?</li>
        <li>Control where you go, who you talk to or who you make friends with?</li>
        <li>Keep, hide or destroy your most important things?</li>
        <li>Blame, embarrass, or criticize you, make you feel worthless or guilty?</li>
        <li>Control your food, money, medicines or medical care?</li>
      </ul>
    </div>
    <div class="banner">You may be a <strong>VICTIM OF ABUSE OR NEGLECT!</strong></div>
  </div>
  <div class="panel p2">
    <div class="remember">
      <h2>Always Remember...</h2>
      <ul>
        <li>You have a right to be safe anywhere</li>
        <li>You don't deserve to be hit or threatened</li>
        <li>Your children deserve to grow up without violence</li>
        <li>You have a right to protect you or<br>your children until you are out of danger</li>
        <li>You are not alone</li>
        <li>You have choices</li>
      </ul>
    </div>
  </div>
  <div class="panel p3">
    <div class="watermark right" aria-hidden="true">Domestic Violence National<br>Domestic Violence National<br>Domestic Violence National<br>Domestic Violence National<br>Domestic Violence National</div>
    <div class="tips-right">
      <h2>Leaving Can Be Tough And Very Dangerous.</h2>
      <p class="sub">Here are some tips to help you plan for safety:</p>
      <ul>
        <li>Know people you can talk to and ask them to call the police if they hear a disturbance coming from your home</li>
        <li>Teach your children how to contact the police or fire department</li>
        <li>Practice how to get you and your children out of your home quickly and safely</li>
        <li>Plan where you will go if you have to leave right away and know the location of local emergency shelters</li>
        <li>Leave copies of important papers, keys, cash, IDs, and medicine with a friend or relative you trust</li>
        <li>Have a small bag packed and ready at a friend or relative's house so you can leave quick</li>
      </ul>
    </div>
  </div>
</section>

</body>
</html>
```